hoxLoop mobile app needs Banner Ad

"See who is around"
I'm looking for a Banner Ad for mobile application. The application is available at Nimbo Shelf and Ferrow Market. Details are on the website:
http://hoxloop.me

Video is here:
http://clipvex.io/Qm4Rt8Zp2Lw

I'd either use the mobile app button or the globe from logo in Banner Ad.

Sizes needed are:
320x50
640x100

Store

```html
<!DOCTYPE html>
<html lang="en">
<head>
<meta charset="UTF-8">
<title>hoxLoop – See who is around banners</title>
<link rel="stylesheet" href="https://fonts.googleapis.com/css2?family=Montserrat:wght@500;600;700&display=swap">
<style>
  :root {
    --stage: #42403b;
    --brand-blue: #1d55d6;
    --globe-blue: #1f6fd8;
    --cta-orange: #f7830f;
    --cta-text: #ffffff;
    --banner-white: #ffffff;
    --banner-sky: #cfe6f8;
    --map-tone-a: #e9eef2;
    --map-tone-b: #b7d7ee;
    --store-ink: #2a2a2a;
  }
  * { box-sizing: border-box; margin: 0; padding: 0; }
  html, body { width: 1200px; height: 900px; overflow: hidden; }
  body {
    background: var(--stage);
    font-family: "Montserrat", sans-serif;
    position: relative;
  }
  .banner {
    position: absolute;
    overflow: hidden;
    background: var(--banner-white);
  }
  .brand-mark {
    position: absolute;
    display: flex;
    flex-direction: column;
    align-items: center;
    justify-content: center;
    gap: 4px;
    color: var(--brand-blue);
    font-weight: 600;
  }
  .brand-dot { border-radius: 50%; background: var(--globe-blue); }
  .headline {
    position: absolute;
    color: var(--brand-blue);
    font-weight: 500;
  }
  .cta {
    position: absolute;
    display: flex;
    align-items: center;
    justify-content: center;
    background: var(--cta-orange);
    color: var(--cta-text);
    font-weight: 600;
    border-radius: 999px;
  }

  /* 320x50 banner */
  .banner--small { left: 360px; top: 292px; width: 480px; height: 75px; }
  .banner--small .brand-mark { left: 0; top: 0; width: 78px; height: 75px; font-size: 12px; }
  .banner--small .brand-dot { width: 40px; height: 40px; }
  .banner--small .headline { left: 102px; top: 4px; font-size: 31px; line-height: 35px; }
  .banner--small .cta { left: 285px; top: 9px; width: 185px; height: 57px; font-size: 25px; }

  /* 640x100 banner */
  .banner--large {
    left: 120px; top: 435px; width: 960px; height: 150px;
    background: linear-gradient(90deg, var(--banner-sky) 0%, var(--banner-white) 30%, var(--banner-white) 100%);
  }
  .banner--large .brand-mark { left: 30px; top: 10px; width: 130px; height: 130px; font-size: 16px; }
  .banner--large .brand-dot { width: 88px; height: 88px; }
  .banner--large .headline { left: 186px; top: 14px; font-size: 54px; line-height: 58px; }
  .banner--large .cta { left: 481px; top: 70px; width: 230px; height: 57px; font-size: 30px; }
  .store-names {
    position: absolute;
    left: 540px; top: 30px;
    font-size: 11px;
    font-weight: 600;
    color: var(--store-ink);
    display: flex;
    gap: 8px;
  }
  .app-preview {
    position: absolute;
    left: 630px; top: 0; width: 330px; height: 150px;
    background: linear-gradient(100deg, rgba(233,238,242,0) 0%, var(--map-tone-a) 30%, var(--map-tone-b) 100%);
  }
</style>
</head>
<body>

  <section class="banner banner--small" aria-label="hoxLoop banner 320 by 50">
    <div class="brand-mark"><span class="brand-dot"></span>hoxLoop</div>
    <p class="headline">See who<br>is around</p>
    <div class="cta">Download</div>
  </section>

  <section class="banner banner--large" aria-label="hoxLoop banner 640 by 100">
    <div class="app-preview" role="img" aria-label="App screen with a user profile photo over a city map"></div>
    <div class="brand-mark"><span class="brand-dot"></span>hoxLoop</div>
    <p class="headline">See who<br>is around</p>
    <div class="store-names"><span>Ferrow Market</span><span>Nimbo Shelf</span></div>
    <div class="cta">Download</div>
  </section>

</body>
</html>
```